Tollo Pollution Mask Packaging

We need a packaging design for a pollution mask, image of mask attached. Have also attached a file with the exact measurements of the box.
There is also an example of a box attached, we would like a similar type design.
I have also attached the Logo, which should be fairly prominent in design.
The following blurb also needed:
Activated carbon dust mask.
99.999% Filtration
Instructions:
1: Place mask over mouth and nose.
2: Ensure aluminium bridge on top.
3: Adjust Gripzo on back to desired tension.
4: Additional Filters sold separately.
Material Description
1: Filter 10% Ammonia
2: N99 Filter Cotton
3: CR Material 100% Neoprene
4: N Cloth 100% Nylon
- RR Beaver

```html
<!DOCTYPE html>
<html lang="en">
<head>
<meta charset="utf-8">
<title>Tollo Activated Carbon Dust Mask – Box Dieline</title>
<link rel="stylesheet" href="https://fonts.googleapis.com/css2?family=Fredoka:wght@500;600&family=Open+Sans:wght@400;700&display=swap">
<style>
  :root {
    --ink: #1b1b1b;
    --lime: #84c341;
    --paper: #ffffff;
    --window: #ffffff;
    --label: #e6e6e6;
    --fold: #3a3a3a;
    --scene-sky: #a7ad9d;
    --scene-green: #5c7a45;
    --scene-dark: #27301f;
  }
  html, body { margin: 0; padding: 0; width: 1200px; height: 849px; overflow: hidden; background: var(--paper); }
  .dieline { display: block; width: 1200px; height: 849px; }
  .panel-ink { fill: var(--ink); }
  .panel-lime { fill: var(--lime); }
  .fold-line { stroke: var(--fold); stroke-width: 0.8; fill: none; }
  .display-type { font-family: "Fredoka", sans-serif; font-weight: 600; }
  .body-type { font-family: "Open Sans", sans-serif; }
  .headline { fill: var(--paper); font-size: 19px; letter-spacing: 0.3px; }
  .brand-name { fill: var(--lime); font-family: "Fredoka", sans-serif; font-weight: 600; }
  .brand-name--dark { fill: var(--ink); }
  .spec-title { fill: var(--ink); font-size: 7.5px; font-weight: 700; }
  .spec-text { fill: var(--ink); font-size: 7.5px; }
  .filtration { fill: var(--lime); font-family: "Fredoka", sans-serif; font-weight: 600; }
  .instr-title { fill: var(--paper); font-size: 11.5px; font-weight: 700; }
  .instr-line { fill: var(--paper); font-size: 9.2px; }
  .side-sub { fill: var(--lime); font-size: 15px; }
  .side-title { fill: var(--lime); font-size: 17px; font-family: "Fredoka", sans-serif; font-weight: 600; }
</style>
</head>
<body>
<svg class="dieline" viewBox="0 0 1160 828" width="1200" height="849" preserveAspectRatio="none" xmlns="http://www.w3.org/2000/svg">
  <defs>
    <linearGradient id="rideSceneTone" x1="0" y1="0" x2="0.6" y2="1">
      <stop offset="0" stop-color="var(--scene-sky)"/>
      <stop offset="0.45" stop-color="var(--scene-green)"/>
      <stop offset="1" stop-color="var(--scene-dark)"/>
    </linearGradient>
  </defs>

  <!-- Front panel with top and bottom tuck flaps -->
  <g class="front">
    <path class="panel-lime" d="M137,258 L137,140 Q137,122 157,122 L467,122 Q487,122 487,140 L487,258 Z"/>
    <path class="panel-lime" d="M137,655 L487,655 L487,768 Q487,785 467,785 L157,785 Q137,785 137,768 Z"/>
    <path class="panel-ink" d="M103,268 Q120,258 140,258 L490,258 L490,655 L140,655 Q120,655 103,645 Z"/>
    <line class="fold-line" x1="137" y1="162" x2="487" y2="162"/>
    <line class="fold-line" x1="137" y1="747" x2="487" y2="747"/>
    <path class="window" fill="var(--window)" d="M230,384 Q290,372 365,386 Q400,394 395,420 Q385,490 330,548 Q300,580 260,580 Q200,578 188,540 Q180,500 196,440 Q205,392 230,384 Z"/>
    <text class="display-type headline" x="155" y="306">ACTIVATED CARBON</text>
    <text class="display-type headline" x="155" y="333">DUST MASK.</text>
    <circle cx="403" cy="322" r="44" fill="var(--lime)"/>
    <text class="brand-name" x="338" y="405" font-size="40" textLength="126" lengthAdjust="spacingAndGlyphs">TOLLO</text>
  </g>

  <!-- Left side panel with dust flaps -->
  <g class="side-left">
    <path class="panel-ink" d="M493,182 L570,178 L572,200 L580,240 L583,250 L583,640 L580,652 L572,690 L570,727 L493,727 Z"/>
    <rect class="panel-lime" x="490" y="250" width="93" height="385"/>
    <g transform="translate(526,446) rotate(90)">
      <text class="body-type spec-title" x="0" y="0" text-anchor="middle">Material Description</text>
    </g>
    <g transform="translate(536,268) rotate(90)">
      <text class="body-type spec-text" x="0" y="0">Filter 10% Ammonia , N99 Filter Cotton ,CR Material 100% Neoprene</text>
      <text class="body-type spec-text" x="0" y="-10">N Cloth 100% Nylon</text>
    </g>
    <g transform="translate(548,570) rotate(90)">
      <text class="brand-name brand-name--dark" x="0" y="0" font-size="22">TOLLO</text>
    </g>
  </g>

  <!-- Back panel with hang tab -->
  <g class="back">
    <path class="panel-ink" d="M597,40 L920,40 L928,60 L935,70 L935,652 L800,652 L795,670 L790,688 L732,688 L727,670 L722,652 L583,652 L583,70 L590,60 Z"/>
    <rect x="744" y="122" width="54" height="11" rx="5.5" fill="var(--paper)"/>
    <rect x="723" y="180" width="96" height="14" rx="7" fill="var(--paper)"/>
    <g transform="translate(770,94) rotate(180)">
      <text class="side-title" x="0" y="0" text-anchor="middle" font-size="18">DUST MASK</text>
      <text class="body-type side-sub" x="0" y="17" text-anchor="middle" font-size="14">Activated carbon</text>
    </g>
    <rect x="621" y="222" width="282" height="170" fill="url(#rideSceneTone)" role="img" aria-label="Photo of a cyclist riding a road bike along a green countryside path"/>
    <text class="filtration" x="621" y="397"><tspan font-size="21">99</tspan><tspan font-size="12">.999% FILTRATION</tspan></text>
    <text class="body-type instr-title" x="622" y="418">Instructions:</text>
    <text class="body-type instr-line" x="622" y="432">1: Place mask over mouth and nose.</text>
    <text class="body-type instr-line" x="622" y="445">2: Ensure aluminium bridge on top.</text>
    <text class="body-type instr-line" x="622" y="458">3: Adjust Gripzo on back to desired tension.</text>
    <text class="body-type instr-line" x="622" y="471">4: Additional Filters sold separately.</text>
    <circle cx="871" cy="436" r="14" fill="var(--lime)"/>
    <text class="brand-name" x="846" y="472" font-size="17">TOLLO</text>
    <rect x="621" y="513" width="282" height="90" fill="var(--label)"/>
    <rect x="730" y="622" width="62" height="26" fill="var(--paper)"/>
  </g>

  <!-- Right side panel with dust flaps -->
  <g class="side-right">
    <path class="panel-ink" d="M935,250 L943,200 L946,182 L1018,178 L1020,200 L1025,240 L1025,655 L1020,690 L1018,727 L946,727 L943,700 L935,652 Z"/>
    <g transform="translate(968,516) rotate(-90)">
      <text class="body-type side-sub" x="0" y="0">Activated carbon</text>
      <text class="side-title" x="0" y="22">DUST MASK</text>
    </g>
  </g>
</svg>
</body>
</html>
```